Homepage Real Estate Agency

I need a web design for a real estate agency in Luxembourg. A short draft for the front page can be found in the project details. (Page 1+2) The main colors of the site should be blue as shown in the project details. (Page 3)
The main target for this site is to promote real estates and a small presentation of the company.

Industry/Entity Type

Real Estate

Requirements
Must have
• On the front page estates are shown in a short preview in small boxes, on the right side is a search. The search is hidden except for the front page. The header has 4 buttons and the logo of the company.

```html
<!DOCTYPE html>
<html lang="fr">
<head>
<meta charset="utf-8">
<title>Clairval – Real Estate Luxembourg</title>
<link href="https://fonts.googleapis.com/css2?family=Arimo:wght@400;700&family=PT+Sans:ital,wght@1,400;1,700&display=swap" rel="stylesheet">
<style>
:root{
  --red:#a21d23; --red-dark:#87151a; --red-light:#bd2a30;
  --navy:#1b3f95; --navy-dark:#0d2a72; --btn-top:#2456b0; --btn-bot:#0a2f7a;
  --lav:#8f92c9; --lav-light:#a9acd9;
  --sky:#3b9ade; --panel:#f4f4f5; --line:#cfcfd4;
  --text:#111; --muted:#6a6a70; --white:#fff;
}
*{box-sizing:border-box;margin:0;padding:0}
html,body{width:1035px;height:1200px;overflow:hidden}
body{font-family:"Arimo",Arial,sans-serif;background:#fff}
.page{position:relative;width:1280px;height:1484px;transform:scale(.80859);transform-origin:0 0;
  background:linear-gradient(180deg,var(--sky) 120px,#7fc1ee 480px,#d8ecfa 900px,#fff 1300px)}
.abs{position:absolute}
.header{left:0;top:0;width:1280px;height:117px;background:linear-gradient(180deg,var(--lav),var(--lav-light))}
.header-rule{left:0;top:117px;width:1280px;height:6px;background:var(--red)}
.brand{left:178px;top:0;width:166px;height:218px;background:linear-gradient(180deg,#ddd 0,#ddd 38px,#eceaec 38px);
  border:3px solid #fff;border-top:none;border-radius:0 0 83px 83px;box-shadow:0 3px 8px rgba(0,0,0,.25);
  display:flex;flex-direction:column;align-items:center;justify-content:center;padding-top:40px;gap:10px}
.brand-dot{width:22px;height:22px;border-radius:50%;background:var(--red)}
.brand-name{font-size:25px;font-weight:700;color:var(--navy-dark)}
.nav{left:387px;top:77px;display:flex;gap:9px}
.nav a{display:block;height:40px;line-height:40px;padding:0 18px;color:#fff;font-size:16px;text-decoration:none;
  background:linear-gradient(180deg,#1f4aa8,#0c2f80)}
.nav a.active{background:linear-gradient(180deg,var(--red-light),var(--red))}
.nav a:nth-child(1){width:105px;text-align:center}
.nav a:nth-child(2){width:125px;text-align:center}
.nav a:nth-child(3){width:89px;text-align:center}
.nav a:nth-child(4){width:89px;text-align:center;padding:0}
.call{right:177px;top:38px;text-align:right;font-family:"PT Sans",sans-serif;font-style:italic;font-weight:700;
  color:#fff;font-size:21px;line-height:27px}
.call span{font-weight:400}
.banner{left:160px;top:123px;width:961px;height:372px;background:linear-gradient(180deg,#15368a,#2a58b3 60%,#3c6fc6)}
.banner-rule{left:160px;top:495px;width:961px;height:5px;background:var(--red)}
.slide{border:6px solid #fff;box-shadow:0 2px 8px rgba(0,0,0,.35)}
.slide-side{top:209px;width:100px;height:213px;background:linear-gradient(180deg,#9fb8d6,#4f6b52 70%,#3e5e2e)}
.slide-main{left:412px;top:167px;width:474px;height:270px;background:linear-gradient(180deg,#b3c3d4,#d6d4cf 45%,#6e6a62 75%,#2f3c26)}
.caption{left:412px;top:437px;width:474px;height:58px;background:linear-gradient(180deg,rgba(255,255,255,.12),rgba(255,255,255,.22));
  color:#fff;font-size:24px;text-align:center;line-height:58px}
.content{left:160px;top:500px;width:961px;height:773px;background:var(--panel);border:1px solid var(--line);border-top:none}
.card{width:252px;height:342px;background:#fff;border:1px solid var(--line);border-top:none}
.card-head{height:41px;background:linear-gradient(180deg,var(--red-light),var(--red));color:#fff;font-weight:700;font-size:18px;
  line-height:41px;padding-left:23px;margin:0 -1px}
.card-photo{height:142px;margin:0 -1px;background:linear-gradient(180deg,#8fb4dd,#d9d2c2 50%,#6f8a3c 78%,#4f7a25)}
.card-title{font-size:18px;color:var(--text);padding:8px 0 0 28px}
.card-meta{font-size:14px;color:var(--muted);padding:8px 0 0 29px;line-height:22px}
.btn{display:block;width:185px;height:45px;line-height:45px;text-align:center;color:#fff;font-size:18px;
  background:linear-gradient(180deg,var(--btn-top),var(--btn-bot));border-radius:2px;text-decoration:none}
.card .btn{position:absolute;left:28px;top:276px}
.search{left:778px;top:528px;width:311px;height:456px;background:var(--panel);border:1px solid var(--line);border-radius:3px}
.search h2{font-weight:400;font-size:20px;color:var(--text);position:absolute;left:22px;top:12px}
.field{position:absolute;right:25px;display:flex;align-items:center;font-size:14px;color:var(--muted)}
.field label{margin-right:8px;text-align:right}
.select{width:157px;height:29px;border:1px solid #ccc;background:#fff;display:flex;font-size:13px;color:#444}
.select span{flex:1;line-height:27px;padding-left:10px}
.select i{width:31px;background:var(--red);display:flex;align-items:center;justify-content:center}
.input{width:157px;height:29px;border:1px solid #ccc;background:#fff}
.search .btn{position:absolute;left:70px;top:378px}
.ptype{left:778px;top:1013px;width:311px;height:228px;background:var(--panel);border:1px solid var(--line);border-top:none}
.ptype .card-head{padding-left:22px}
.ptype ul{list-style:none;padding:14px 0 0 17px}
.ptype li{font-size:14px;color:var(--muted);height:25px;display:flex;align-items:center;gap:8px}
.footer{left:158px;top:1287px;width:966px;height:149px;background:var(--red)}
.fcol{position:absolute;top:17px;color:#fff}
.fcol h3{font-size:14px;font-weight:700;letter-spacing:.5px;margin-bottom:12px}
.fcol ul{list-style:none}
.fcol li{font-size:13px;height:22px;display:flex;align-items:center;gap:8px}
.fdiv{position:absolute;left:604px;top:6px;width:1px;height:136px;background:rgba(255,255,255,.3)}
.fcall{position:absolute;left:667px;top:34px;color:#fff;font-family:"PT Sans",sans-serif;font-style:italic;font-weight:700;font-size:21px;line-height:27px}
.fcall span{font-weight:400}
.fphone{position:absolute;left:667px;top:68px}
.femail{position:absolute;left:731px;top:94px;color:#fff;font-size:13px}
.copy{left:0;top:1451px;width:1280px;text-align:center;font-size:13px;color:#666;padding-right:75px}
</style>
</head>
<body>
<div class="page">
  <div class="abs header"></div>
  <div class="abs header-rule"></div>

  <div class="abs banner"></div>
  <div class="abs banner-rule"></div>
  <svg class="abs" style="left:226px;top:265px" width="44" height="72" viewBox="0 0 44 72"><path d="M44 0 0 36 44 72Z" fill="#5a7fc8" opacity=".8"/></svg>
  <svg class="abs" style="left:1042px;top:265px" width="44" height="72" viewBox="0 0 44 72"><path d="M0 0 44 36 0 72Z" fill="#5a7fc8" opacity=".8"/></svg>
  <div class="abs slide slide-side" style="left:312px" role="img" aria-label="Photo of a house with garage"></div>
  <div class="abs slide slide-side" style="left:878px" role="img" aria-label="Photo of a house with garden"></div>
  <div class="abs slide slide-main" role="img" aria-label="Photo of a large white house with dormer windows"></div>
  <div class="abs caption">The best place to buy new proparty</div>

  <div class="abs brand"><span class="brand-dot"></span><span class="brand-name">Clairval</span></div>
  <nav class="abs nav">
    <a class="active" href="#">A vendre</a><a href="#">Construction</a><a href="#">Location</a><a href="#">Cherchns</a>
  </nav>
  <div class="abs call">Call us: <span>+352-20-45-1077</span><br><span>+352-20-45-1078</span></div>

  <div class="abs content"></div>

  <div class="abs card" style="left:201px;top:527px">
    <div class="card-head">Alder Enclave</div>
    <div class="card-photo" role="img" aria-label="Photo of a two-storey family house"></div>
    <div class="card-title">Pallavaram,Luxembourg</div>
    <div class="card-meta">Built Up Area : 1200 Sq. Feet<br>Bedrooms : 3</div>
    <a class="btn" href="#">Read more</a>
  </div>
  <div class="abs card" style="left:490px;top:528px">
    <div class="card-head">Alder Enclave</div>
    <div class="card-photo" role="img" aria-label="Photo of a single-storey house with lawn"></div>
    <div class="card-title">Pallavaram, Luxembourg</div>
    <div class="card-meta">Built Up Area : 1200 Sq. Feet<br>Bedrooms : 3</div>
    <a class="btn" href="#">Read more</a>
  </div>
  <div class="abs card" style="left:201px;top:901px">
    <div class="card-head">Alder Enclave</div>
    <div class="card-photo" role="img" aria-label="Photo of a large villa with porch"></div>
    <div class="card-title">Pallavaram, Luxembourg</div>
    <div class="card-meta">Built Up Area : 1200 Sq. Feet<br>Bedrooms : 3</div>
    <a class="btn" href="#">Read more</a>
  </div>
  <div class="abs card" style="left:490px;top:901px">
    <div class="card-head">Alder Enclave</div>
    <div class="card-photo" role="img" aria-label="Photo of a two-storey family house"></div>
    <div class="card-title">Pallavaram, Luxembourg</div>
    <div class="card-meta">Built Up Area : 1200 Sq. Feet<br>Bedrooms : 3</div>
    <a class="btn" href="#">Read more</a>
  </div>

  <div class="abs search">
    <h2>Search your proparties</h2>
    <div class="field" style="top:62px"><label>Property Type :</label><div class="select"><span>All Residential</span><i><svg width="10" height="7"><path d="M0 0h10L5 7z" fill="#fff"/></svg></i></div></div>
    <div class="field" style="top:112px"><label>Your City :</label><div class="select"><span>Select city</span><i><svg width="10" height="7"><path d="M0 0h10L5 7z" fill="#fff"/></svg></i></div></div>
    <div class="field" style="top:162px"><label>Price range :</label><div class="select"><span>Selct price range</span><i><svg width="10" height="7"><path d="M0 0h10L5 7z" fill="#fff"/></svg></i></div></div>
    <div class="field" style="top:212px"><label>Bed rooms :</label><div class="select"><span>Select beddrooms</span><i><svg width="10" height="7"><path d="M0 0h10L5 7z" fill="#fff"/></svg></i></div></div>
    <div class="field" style="top:262px"><label>Bath rooms :</label><div class="select"><span>Select bath rooms</span><i><svg width="10" height="7"><path d="M0 0h10L5 7z" fill="#fff"/></svg></i></div></div>
    <div class="field" style="top:311px"><label>Keywords :</label><div class="input"></div></div>
    <a class="btn" href="#">Search</a>
  </div>

  <div class="abs ptype">
    <div class="card-head">Property Type</div>
    <ul>
      <li><svg width="5" height="9"><path d="M0 0l5 4.5L0 9z" fill="#a21d23"/></svg>Apartment (240)</li>
      <li><svg width="5" height="9"><path d="M0 0l5 4.5L0 9z" fill="#a21d23"/></svg>Independent House/Villa (51)</li>
      <li><svg width="5" height="9"><path d="M0 0l5 4.5L0 9z" fill="#a21d23"/></svg>Residential Land (89)</li>
      <li><svg width="5" height="9"><path d="M0 0l5 4.5L0 9z" fill="#a21d23"/></svg>Commercial Building (6)</li>
      <li><svg width="5" height="9"><path d="M0 0l5 4.5L0 9z" fill="#a21d23"/></svg>Office Complex (3)</li>
      <li><svg width="5" height="9"><path d="M0 0l5 4.5L0 9z" fill="#a21d23"/></svg>Commercial Land (2)</li>
    </ul>
  </div>

  <footer class="abs footer">
    <div class="fcol" style="left:25px"><h3>HOT &nbsp;LOCATIONS</h3><ul>
      <li><svg width="5" height="9"><path d="M0 0l5 4.5L0 9z" fill="#fff"/></svg>OMR</li>
      <li><svg width="5" height="9"><path d="M0 0l5 4.5L0 9z" fill="#fff"/></svg>GST Road</li>
      <li><svg width="5" height="9"><path d="M0 0l5 4.5L0 9z" fill="#fff"/></svg>Sriperumpudur</li>
      <li><svg width="5" height="9"><path d="M0 0l5 4.5L0 9z" fill="#fff"/></svg>Adyar</li></ul></div>
    <div class="fcol" style="left:190px"><h3>FEATURED &nbsp;BUILDERS</h3><ul>
      <li><svg width="5" height="9"><path d="M0 0l5 4.5L0 9z" fill="#fff"/></svg>Rivane Housing</li>
      <li><svg width="5" height="9"><path d="M0 0l5 4.5L0 9z" fill="#fff"/></svg>Hollis Group</li>
      <li><svg width="5" height="9"><path d="M0 0l5 4.5L0 9z" fill="#fff"/></svg>K Sorel Builder...</li>
      <li><svg width="5" height="9"><path d="M0 0l5 4.5L0 9z" fill="#fff"/></svg>Terrace Ambiance</li></ul></div>
    <div class="fcol" style="left:382px"><h3>FEATURED &nbsp;PROJECTS</h3><ul>
      <li><svg width="5" height="9"><path d="M0 0l5 4.5L0 9z" fill="#fff"/></svg>Prairie Acres</li>
      <li><svg width="5" height="9"><path d="M0 0l5 4.5L0 9z" fill="#fff"/></svg>Solvane Residen...</li>
      <li><svg width="5" height="9"><path d="M0 0l5 4.5L0 9z" fill="#fff"/></svg>Perle Galaxy</li>
      <li><svg width="5" height="9"><path d="M0 0l5 4.5L0 9z" fill="#fff"/></svg>Greenvale Cit...</li></ul></div>
    <div class="fdiv"></div>
    <div class="fcall">Call us: <span>+352-20-45-1077</span><br><span style="padding-left:64px">+352-20-45-1078</span></div>
    <svg class="fphone" width="54" height="40" viewBox="0 0 54 40" aria-hidden="true">
      <path d="M2 12C8 2 46 2 52 12l-2 7-10-2v-5c-7-3-19-3-26 0v5L4 19z" fill="#e7a3a5"/>
      <path d="M14 18h26l8 20H6z" fill="#e7a3a5"/><circle cx="27" cy="28" r="5" fill="#a21d23"/>
    </svg>
    <div class="femail">email: info@clairval.lu</div>
  </footer>
  <div class="abs copy">Copyright © 2012 . All rights reserved.</div>
</div>
</body>
</html>
```